Brantwell Group needs a business card design

We need a new business card design using the logo recently selected in a logo competition on Pixel Forum. Our business is a consultancy specializing in aviation and energy and the winning business card design will promote an image of precision and professionalism with creativity.

Please use the logo with the name on the front of the card and use a complementary font. Make the back white with either the light grey or dark grey logo.

Target Market(s)

Senior finance and legal leaders at aviation and energy companies

Industry/Entity Type

Management Consulting

Contact Information for Business Card

Peter Haldane
President
Brantwell Group

www.brantwellgroup.example

(555) 304-6198
ph@brantwellgroup.example

Requirements
Must have
• Professional font that goes well with the logo font

```html
<!DOCTYPE html>
<html lang="en">
<head>
<meta charset="utf-8">
<title>Brantwell Group – Business Card</title>
<link rel="stylesheet" href="https://fonts.googleapis.com/css2?family=Alegreya+Sans:ital,wght@0,300;1,300;1,400&display=swap">
<style>
  :root {
    --navy: #123f73;
    --navy-stripe: #5a7fa8;
    --grey-light: #e7e7e7;
    --grey-faint: #f2f2f2;
    --grey-mark: #e0e0e0;
    --grey-text: #6b6b6b;
    --white: #ffffff;
    --stage: #2b2b2b;
  }
  * { box-sizing: border-box; margin: 0; padding: 0; }
  html, body {
    width: 1200px;
    height: 1000px;
    overflow: hidden;
    background: var(--stage);
  }
  .sheet {
    position: relative;
    width: 1200px;
    height: 1000px;
    display: flex;
    justify-content: center;
    align-items: center;
    gap: 120px;
  }
  .card {
    width: 360px;
    height: 630px;
    background: var(--white);
    position: relative;
    overflow: hidden;
  }
  .card svg { display: block; }
  .wordmark {
    font-family: "Alegreya Sans", sans-serif;
    font-weight: 300;
    fill: var(--navy);
  }
  .contact {
    font-family: "Alegreya Sans", sans-serif;
    font-style: italic;
    font-weight: 300;
    fill: var(--white);
  }
  .contact-name { font-size: 30px; font-weight: 400; }
  .contact-role { font-size: 16px; }
  .contact-line { font-size: 15px; }
  .back-wordmark {
    font-family: "Alegreya Sans", sans-serif;
    font-weight: 300;
    fill: var(--grey-mark);
  }
</style>
</head>
<body>
<main class="sheet">

  <!-- Front of card -->
  <section class="card card-front" aria-label="Business card front">
    <svg width="360" height="630" viewBox="0 0 360 630">
      <defs>
        <pattern id="stripes" width="8" height="8" patternUnits="userSpaceOnUse" patternTransform="rotate(20)">
          <rect width="8" height="8" fill="var(--navy)"/>
          <rect width="2" height="8" fill="var(--navy-stripe)"/>
        </pattern>
      </defs>

      <!-- top decorative blocks -->
      <g class="top-blocks">
        <rect x="0" y="0" width="150" height="240" fill="var(--grey-light)"/>
        <polygon points="0,0 360,0 360,40 230,90 0,90" fill="url(#stripes)"/>
        <polygon points="150,0 360,0 360,70 150,140" fill="var(--navy)"/>
        <polygon points="0,90 120,90 120,190 0,230" fill="var(--navy)"/>
      </g>

      <!-- wordmark -->
      <g class="brand">
        <text class="wordmark" x="40" y="320" font-size="54" letter-spacing="1">BRANTWELL</text>
        <text class="wordmark" x="44" y="360" font-size="24" letter-spacing="24">GROUP</text>
      </g>

      <!-- contact band -->
      <g class="contact-band">
        <polygon points="0,440 360,360 360,630 0,630" fill="var(--navy)"/>
        <polygon points="300,630 360,560 360,630" fill="url(#stripes)"/>
        <text class="contact contact-name" x="40" y="480">Peter Haldane</text>
        <text class="contact contact-role" x="40" y="504">President Brantwell Group</text>

        <g class="contact-icons" fill="var(--white)">
          <circle cx="48" cy="537" r="7"/>
          <rect x="41" y="552" width="14" height="14" rx="2"/>
          <rect x="41" y="576" width="14" height="14" rx="2"/>
        </g>
        <g class="icon-glyphs" stroke="var(--navy)" stroke-width="1.3" fill="none">
          <ellipse cx="48" cy="537" rx="3" ry="6"/>
          <line x1="42" y1="537" x2="54" y2="537"/>
          <path d="M45 555 q0 8 6 9 l1 -2 -2 -2 -1 1 q-2 -1 -3 -3 l1 -1 -2 -2 z" fill="var(--navy)" stroke="none"/>
          <rect x="44" y="580" width="8" height="6"/>
          <polyline points="44,580 48,584 52,580"/>
        </g>
        <text class="contact contact-line" x="66" y="542">www.brantwellgroup.example</text>
        <text class="contact contact-line" x="66" y="564">(555) 304-6198</text>
        <text class="contact contact-line" x="66" y="588">ph@brantwellgroup.example</text>
      </g>
    </svg>
  </section>

  <!-- Back of card -->
  <section class="card card-back" aria-label="Business card back">
    <svg width="360" height="630" viewBox="0 0 360 630">
      <rect x="0" y="0" width="360" height="630" fill="var(--grey-faint)" role="img" aria-label="Faint repeating pattern of the group mark"/>
      <text class="back-wordmark" x="180" y="310" font-size="48" text-anchor="middle">BRANTWELL</text>
      <text class="back-wordmark" x="192" y="350" font-size="22" letter-spacing="20" text-anchor="middle">GROUP</text>
    </svg>
  </section>

</main>
</body>
</html>
```